Fennimore Glen Books -- young adult, fantasy for small publisher looking for long term relationship fo

THE GLASS TOWER.
YA fantasy. Tolin, black hair, grey eyes, lives alone in a decaying red metropolis. Alone that is except for the body drifting slowly to shore and the shadows who look after him, tutor him, etc. He will have to fight against a non-human army if he is to win his way off the island and THE GLASS TOWER.
AUTHOR -- JOSEPH R. QUINTON
SERIES -- CHRONICLE OF THE HOLLOW PEAKS
book size -- 5 x 8

Target Market(s)

Age 12+ boys, adults who read fantasy

Industry/Entity Type

Book Publisher

Requirements
Must have
• red city in background, boy's face -- black hair, grey eyes, sea (if possible). I need something that will POP on North American bookshelves, something that will scream out BUY ME BUY ME!!!

```html
<!DOCTYPE html>
<html lang="en">
<head>
<meta charset="utf-8">
<title>The Glass Tower — Back Cover</title>
<link rel="stylesheet" href="https://fonts.googleapis.com/css2?family=Arimo&family=Orbitron:wght@700;900&family=Rubik+Dirt&family=Rubik+Wet+Paint&display=swap">
<style>
  :root {
    --red-bright: #e0100c;
    --red-mid: #b0060a;
    --red-dark: #6e0206;
    --red-deep: #2a0002;
    --black: #000000;
    --white: #ffffff;
    --cyan: #27d3e6;
    --title-red: #d51414;
  }
  * { margin: 0; padding: 0; box-sizing: border-box; }
  html, body { width: 750px; height: 1200px; overflow: hidden; background: var(--black); }
  .back-cover {
    position: relative;
    width: 750px;
    height: 1200px;
    overflow: hidden;
    color: var(--white);
    font-family: "Arimo", Arial, sans-serif;
    background: var(--black);
  }
  .city-art {
    position: absolute;
    left: 0;
    top: 0;
    width: 750px;
    height: 900px;
    background:
      radial-gradient(ellipse 55% 30% at 50% 20%, rgba(255,70,50,0.45), transparent 70%),
      radial-gradient(ellipse 30% 40% at 8% 55%, rgba(40,0,0,0.55), transparent 70%),
      radial-gradient(ellipse 25% 35% at 95% 50%, rgba(40,0,0,0.5), transparent 70%),
      linear-gradient(180deg, var(--red-bright) 0%, #cf0b0b 30%, var(--red-mid) 50%, #8e0308 65%, var(--red-dark) 78%, var(--red-deep) 92%, var(--black) 100%);
  }
  .sea-art {
    position: absolute;
    left: 0;
    top: 690px;
    width: 750px;
    height: 210px;
    background: linear-gradient(180deg, rgba(60,0,4,0) 0%, rgba(60,0,4,0.55) 35%, rgba(20,0,1,0.85) 75%, var(--black) 100%);
  }
  .title {
    position: absolute;
    top: 70px;
    left: 0;
    width: 100%;
    text-align: center;
    font-family: "Rubik Wet Paint", Impact, sans-serif;
    font-weight: normal;
    font-size: 70px;
    line-height: 1;
    color: var(--title-red);
    -webkit-text-stroke: 4px var(--white);
    paint-order: stroke fill;
    text-shadow: 3px 4px 5px rgba(0,0,0,0.65);
    letter-spacing: 1px;
  }
  .series {
    position: absolute;
    top: 178px;
    left: 0;
    width: 100%;
    text-align: center;
    font-family: "Orbitron", sans-serif;
    font-weight: 900;
    font-size: 13px;
    letter-spacing: 0.3px;
    color: var(--cyan);
  }
  .synopsis {
    position: absolute;
    top: 249px;
    left: 55px;
    width: 640px;
    text-align: center;
    font-size: 18.5px;
    line-height: 22.5px;
  }
  .synopsis-heading {
    font-weight: normal;
    font-size: 18px;
    line-height: 22px;
  }
  .synopsis p + p { margin-top: 22.5px; }
  .author-name {
    position: absolute;
    top: 756px;
    left: 0;
    width: 100%;
    text-align: center;
    font-family: "Rubik Dirt", Impact, sans-serif;
    font-weight: normal;
    font-size: 38px;
    line-height: 1.1;
    letter-spacing: 0.5px;
  }
  .author-bio {
    position: absolute;
    top: 846px;
    left: 65px;
    width: 620px;
    text-align: center;
    font-size: 18.5px;
    line-height: 23px;
  }
  .publisher {
    position: absolute;
    top: 1012px;
    left: 258px;
    width: 286px;
    height: 84px;
    display: flex;
    align-items: center;
    justify-content: center;
    text-align: center;
    font-size: 34px;
    line-height: 38px;
    color: var(--white);
  }
</style>
</head>
<body>
  <main class="back-cover">
    <div class="city-art" role="img" aria-label="Decaying red metropolis skyline with shadowy figures looming among the towers"></div>
    <div class="sea-art" role="img" aria-label="Dark red sea at the city's shore, a body drifting toward land"></div>

    <h1 class="title">GLASS TOWER</h1>
    <div class="series">CHRONICLE OF THE HOLLOW PEAKS</div>

    <section class="synopsis">
      <h2 class="synopsis-heading">SYNOPSIS</h2>
      <p>Tolin lives alone in a decaying red metropolis at the edge of a restless sea. Alone, that is, except for the body drifting slowly to shore and the shadows who look after him, feed him and tutor him in the old ways of the city.</p>
      <p>But the shadows are not the only things that stir among the ruins. Beyond the crumbling towers a non-human army gathers, and its march grows closer with every tide. To survive, Tolin must learn what the shadows have kept from him, who the drowned stranger was, and why the city bleeds red beneath a silent sky. Every street holds a secret, every tower a trap. If he is to win his way off the island, he will have to fight for every step against enemies that do not sleep, do not tire and do not forget. Only then can he reach the one place that may hold the truth: the Glass Tower.</p>
    </section>

    <h2 class="author-name">JOSEPH R. QUINTON</h2>

    <p class="author-bio">Joseph R. Quinton grew up on a windswept coast, reading every fantasy novel he could find. He writes stories of lonely heroes, forgotten cities and the sea. He lives with his family and far too many books.</p>

    <div class="publisher">Fennimore Glen<br>Books</div>
  </main>
</body>
</html>
```